Freelance business trainer needs a new business card

My business is called Tbrite. I provide training in the workplace on management, coaching and mentoring, and customer service topics for a variety of businesses, colleges and private training providers, and teach on management programs. I need a professional but eye catching business card. Business colours grey and orange. My name Linda Marchbank; Tel 07853 416207; email lmarchbank@tbrite.co.uk; website www.tbrite.co.uk.
Happy to have some sort of logo on front and details on back or all on one side
Target Market(s)
SME businesses and colleges - workshops i run are for adults in the workplace
Industry/Entity Type
Training
Look and feel

```html
<!DOCTYPE html>
<html lang="en">
<head>
<meta charset="utf-8">
<title>Tbrite business card designs</title>
<link href="https://fonts.googleapis.com/css2?family=Poppins:wght@400;600;700&family=Merriweather:wght@900&display=swap" rel="stylesheet">
<style>
  :root {
    --orange: #f7931e;
    --grey: #4a4a4a;
    --grey-dark: #2f2f2f;
    --white: #ffffff;
    --stage: #3b302b;
  }
  * { box-sizing: border-box; margin: 0; padding: 0; }
  html, body { width: 1200px; height: 900px; overflow: hidden; }
  body {
    position: relative;
    background: var(--stage);
    font-family: "Poppins", sans-serif;
  }
  .design-label {
    position: absolute;
    color: var(--white);
    font-family: "Merriweather", serif;
    font-weight: 900;
    font-size: 40px;
  }
  .design-label--one { left: 110px; top: 45px; }
  .design-label--two { left: 690px; top: 800px; }

  .card {
    position: absolute;
    width: 500px;
    height: 290px;
    background: var(--white);
    overflow: hidden;
    box-shadow: 0 8px 18px rgba(0,0,0,.45);
  }
  .row-one .card { top: 120px; }
  .row-two .card { top: 480px; }
  .card--about { left: 60px; }
  .card--contact { left: 640px; }

  .stripe, .panel { position: absolute; top: 0; height: 100%; background: var(--orange); }
  .stripe { width: 10px; }

  /* about side */
  .card--about .stripe--a { left: 275px; }
  .card--about .stripe--b { left: 293px; }
  .card--about .panel { left: 311px; right: 0; }
  .about-text {
    position: absolute;
    left: 28px; top: 62px; width: 240px;
    font-size: 10.5px; font-weight: 700; line-height: 2.05;
    color: var(--orange);
  }
  .about-text .brand-inline { color: var(--grey-dark); }

  .brand-name {
    position: absolute;
    font-weight: 700;
    color: var(--grey);
    letter-spacing: .5px;
  }
  .card--about .brand-name { left: 330px; font-size: 30px; }
  .row-one .card--about .brand-name { top: 20px; }
  .row-two .card--about .brand-name { top: 110px; left: 345px; }

  /* contact side */
  .card--contact .panel { left: 0; width: 250px; }
  .card--contact .stripe--a { left: 258px; }
  .card--contact .stripe--b { left: 276px; }
  .card--contact .brand-name { font-size: 38px; }
  .row-one .card--contact .brand-name { left: 28px; top: 22px; }
  .row-two .card--contact .brand-name { left: 50px; top: 112px; }

  .person { position: absolute; right: 26px; top: 78px; text-align: right; }
  .person-name { color: var(--orange); font-weight: 700; font-size: 14px; }
  .person-role, .person-creds { color: var(--grey); font-size: 9.5px; line-height: 1.5; }

  .contact-list {
    position: absolute; right: 26px; bottom: 28px;
    list-style: none; text-align: right;
  }
  .contact-item {
    display: flex; justify-content: flex-end; align-items: center; gap: 6px;
    font-size: 10.5px; font-weight: 700; color: var(--grey-dark);
    margin-top: 8px;
  }
  .contact-icon { width: 16px; height: 16px; display: block; }
</style>
</head>
<body>
  <div class="design-label design-label--one">Design 1</div>
  <div class="design-label design-label--two">Design 2</div>

  <section class="row-one">
    <article class="card card--about">
      <p class="about-text"><span class="brand-inline">Tbrite</span> provides a range of workplace management &amp;business training, empowering &amp; encouragin employees to fully utilise skills &amp; knowledge learnt to enhance thier working practices &amp; achieve objectives.</p>
      <div class="stripe stripe--a"></div>
      <div class="stripe stripe--b"></div>
      <div class="panel"></div>
      <div class="brand-name">Tbrite</div>
    </article>
    <article class="card card--contact">
      <div class="panel"></div>
      <div class="stripe stripe--a"></div>
      <div class="stripe stripe--b"></div>
      <div class="brand-name">Tbrite</div>
      <div class="person">
        <div class="person-name">Linda Marchbank</div>
        <div class="person-role">Owner/Lead Trainer</div>
        <div class="person-creds">MCMI, MIFL, CertEd, PGCCM, TIOSH</div>
      </div>
      <ul class="contact-list">
        <li class="contact-item">07853 416207
          <svg class="contact-icon" viewBox="0 0 16 16"><rect width="16" height="16" fill="#f7931e"/><rect x="5" y="3" width="6" height="10" rx="1" fill="none" stroke="#fff" stroke-width="1.3"/></svg></li>
        <li class="contact-item">lmarchbank@tbrite.co.uk
          <svg class="contact-icon" viewBox="0 0 16 16"><rect width="16" height="16" fill="#f7931e"/><rect x="3" y="4.5" width="10" height="7" fill="none" stroke="#fff" stroke-width="1.2"/><path d="M3 4.5 8 8.5 13 4.5" fill="none" stroke="#fff" stroke-width="1.2"/></svg></li>
        <li class="contact-item">www.tbrite.co.uk.
          <svg class="contact-icon" viewBox="0 0 16 16"><rect width="16" height="16" fill="#f7931e"/><circle cx="8" cy="8" r="4.5" fill="none" stroke="#fff" stroke-width="1.2"/><path d="M3.5 8h9M8 3.5v9" stroke="#fff" stroke-width="1"/></svg></li>
      </ul>
    </article>
  </section>

  <section class="row-two">
    <article class="card card--about">
      <p class="about-text"><span class="brand-inline">Tbrite</span> provides a range of workplace management &amp;business training, empowering &amp; encouragin employees to fully utilise skills &amp; knowledge learnt to enhance thier working practices &amp; achieve objectives.</p>
      <div class="stripe stripe--a"></div>
      <div class="stripe stripe--b"></div>
      <div class="panel"></div>
      <div class="brand-name">Tbrite</div>
    </article>
    <article class="card card--contact">
      <div class="panel"></div>
      <div class="stripe stripe--a"></div>
      <div class="stripe stripe--b"></div>
      <div class="brand-name">Tbrite</div>
      <div class="person">
        <div class="person-name">Linda Marchbank</div>
        <div class="person-role">Owner/Lead Trainer</div>
        <div class="person-creds">MCMI, MIFL, CertEd, PGCCM, TIOSH</div>
      </div>
      <ul class="contact-list">
        <li class="contact-item">07853 416207
          <svg class="contact-icon" viewBox="0 0 16 16"><rect width="16" height="16" fill="#f7931e"/><rect x="5" y="3" width="6" height="10" rx="1" fill="none" stroke="#fff" stroke-width="1.3"/></svg></li>
        <li class="contact-item">lmarchbank@tbrite.co.uk
          <svg class="contact-icon" viewBox="0 0 16 16"><rect width="16" height="16" fill="#f7931e"/><rect x="3" y="4.5" width="10" height="7" fill="none" stroke="#fff" stroke-width="1.2"/><path d="M3 4.5 8 8.5 13 4.5" fill="none" stroke="#fff" stroke-width="1.2"/></svg></li>
        <li class="contact-item">www.tbrite.co.uk.
          <svg class="contact-icon" viewBox="0 0 16 16"><rect width="16" height="16" fill="#f7931e"/><circle cx="8" cy="8" r="4.5" fill="none" stroke="#fff" stroke-width="1.2"/><path d="M3.5 8h9M8 3.5v9" stroke="#fff" stroke-width="1"/></svg></li>
      </ul>
    </article>
  </section>
</body>
</html>
```